3.5" x 11" Door Hanger Design - Residential Roofing Company

We are looking for a double-sided door hanger that we can hang on the doors of prospects. This door hanger would have some brief information about our company, a phone number, website, and then the services that we offer. I don't know that it will have enough room for a lot of pictures, but feel free to use those from the marketing brochure if you think it'll work and I can get you the original as needed.
I have uploaded our certifications, logo, and then our current marketing brochure. The design should be cohesive with our marketing brochure, but doesn't have to match it perfectly.
Lastly, attached is the template that we are planning to print off of. This has a tear off portion at the bottom for a business card for a sales rep. The size of the overall door hanger will be 3.5" x 11", with the bottom 2.5" being the tear off business card with the salesman's information. I'll get you the sales reps information during the final design phase, but we will need name, title, phone number, email, business address, business website, list of services, and then the words "QX LBN 602715" all on that small portion as well so if they tear it off they still have all the info.

```html
<!DOCTYPE html>
<html lang="en">
<head>
<meta charset="utf-8">
<title>Mesa Ridge Roofing – Door Hanger</title>
<link href="https://fonts.googleapis.com/css2?family=Roboto+Slab:wght@800&family=Roboto:ital,wght@0,400;0,500;0,700;1,400&display=swap" rel="stylesheet">
<style>
  :root{
    --stage:#707070;
    --ink:#1c1b1b;
    --orange:#e4591f;
    --white:#ffffff;
    --grey-text:#555555;
    --sky-grey:#9aa0ad;
    --sky-blue:#4f7fbf;
  }
  *{box-sizing:border-box;margin:0;padding:0}
  html,body{width:835px;height:1200px;overflow:hidden;background:var(--stage)}
  body{position:relative;font-family:"Roboto",Arial,sans-serif}
  .hanger{position:absolute;width:334px;height:1000px;overflow:hidden;background:var(--ink);box-shadow:0 2px 6px rgba(0,0,0,.35)}
  .hanger--front{left:64px;top:65px}
  .hanger--back{left:444px;top:72px}
  .abs{position:absolute}
  .center{left:0;right:0;text-align:center}
  .hole{position:absolute;left:111px;top:79px;width:112px;height:112px;border-radius:50%;background:var(--white)}
  .photo{position:absolute;left:0;top:0;width:334px}
  .front-photo{height:620px;background:linear-gradient(180deg,#8c93a3 0%,#a4a9b5 35%,#8b8a86 55%,#77736b 72%,#8f8a80 100%)}
  .back-photo{height:560px;background:linear-gradient(180deg,#9dbbe0 0%,#5f8fcc 30%,#6c94c8 50%,#6b5a46 68%,#4a3a2c 85%,#3a3129 100%)}
  .brand-name{font-family:"Roboto Slab",Georgia,serif;font-weight:800;letter-spacing:.2px;white-space:nowrap}
  .slab{font-family:"Roboto Slab",Georgia,serif;font-weight:800}
  .chevrons{position:absolute;left:0;top:0}
  .headline{font-size:22px;line-height:29px;letter-spacing:.3px}
  .headline .white{color:var(--white)}
  .headline .orange{color:var(--orange)}
  .rule{position:absolute;left:157px;top:673px;width:22px;height:1px;background:var(--orange)}
  .call-now{top:688px;font-size:17px;color:var(--white)}
  .front-phone{top:711px;font-size:27px;font-weight:500;color:var(--orange)}
  .web-button{position:absolute;left:58px;top:757px;width:217px;height:28px;border-radius:14px;background:var(--orange);color:var(--white);font-size:10px;text-align:center;line-height:28px;letter-spacing:.3px}
  .tear-card{position:absolute;left:0;top:812px;width:334px;height:188px;background:var(--white)}
  .card-brand{position:absolute;left:46px;top:100px;font-size:13px;color:var(--ink)}
  .card-divider{position:absolute;left:175px;top:50px;width:1px;height:90px;background:#9a9a9a}
  .rep{position:absolute;left:185px;top:48px;font-size:7.5px;line-height:10px;color:#333}
  .rep .rep-name{font-size:11px;font-weight:700;color:var(--orange);line-height:13px}
  .rep .rep-title{color:var(--grey-text)}
  .rep .gap{height:4px}
  .rep .contact{display:flex;align-items:center;gap:4px}
  .rep svg{flex:none}
  .quality{left:138px;width:190px;text-align:center;font-size:29px;line-height:33px;color:var(--orange)}
  .trust{left:120px;width:214px;top:548px;text-align:center;font-size:25px;font-style:italic;color:var(--white)}
  .types{position:absolute;left:0;top:585px}
  .type-label{position:absolute;top:712px;font-size:7.5px;color:var(--white);transform:translateX(-50%);letter-spacing:.2px}
  .phone-strip{position:absolute;left:0;top:736px;width:334px;height:34px;background:var(--white);display:flex;align-items:center;justify-content:center;gap:9px}
  .phone-strip span{font-size:21px;font-weight:500;color:var(--ink)}
  .back-address{top:776px;font-size:12px;color:var(--white)}
  .back-brand{top:965px;top:900px;font-size:26px;color:var(--white)}
  .tagline{top:948px;font-size:12px;color:var(--white)}
</style>
</head>
<body>

<!-- Front side -->
<section class="hanger hanger--front">
  <div class="photo front-photo" role="img" aria-label="Photo of a stone and wood-sided home with a grey tile roof under a cloudy sky"></div>
  <div class="hole"></div>
  <div class="abs center brand-name" style="top:292px;font-size:27px;color:var(--ink)">Mesa Ridge Roofing</div>

  <svg class="chevrons" width="334" height="1000" viewBox="0 0 334 1000">
    <polygon points="0,590 255,484 334,522 334,1000 0,1000" fill="#1c1b1b"/>
    <polyline points="0,585 255,479 334,517" fill="none" stroke="#e4591f" stroke-width="8"/>
    <polyline points="0,560 82,524 110,538" fill="none" stroke="#e4591f" stroke-width="7"/>
  </svg>

  <div class="abs center headline slab" style="top:576px">
    <div class="white">INSTALLING</div>
    <div class="orange">QUALITY ROOFS</div>
    <div class="orange">ACROSS ARIZONA</div>
  </div>
  <div class="rule"></div>
  <div class="abs center call-now">Call Now</div>
  <div class="abs center front-phone">(555) 214 7730</div>
  <div class="web-button slab">WWW.MESARIDGE-ROOFING.COM</div>

  <div class="tear-card">
    <div class="card-brand brand-name">Mesa Ridge Roofing</div>
    <div class="card-divider"></div>
    <div class="rep">
      <div class="rep-name">Dana Whitfield</div>
      <div class="rep-title">President</div>
      <div class="gap"></div>
      <div>QX LBN 602715</div>
      <div class="gap"></div>
      <div>1420 Pinecrest Ave</div>
      <div>Alder AZ 86999</div>
      <div class="gap"></div>
      <div class="contact"><svg width="7" height="7" viewBox="0 0 24 24"><path fill="#e4591f" d="M6.6 10.8a15 15 0 0 0 6.6 6.6l2.2-2.2a1 1 0 0 1 1-.25 11.4 11.4 0 0 0 3.6.57 1 1 0 0 1 1 1V20a1 1 0 0 1-1 1A17 17 0 0 1 3 4a1 1 0 0 1 1-1h3.5a1 1 0 0 1 1 1c0 1.25.2 2.45.57 3.57a1 1 0 0 1-.25 1z"/></svg>(555) 214-7730</div>
      <div class="contact"><svg width="7" height="6" viewBox="0 0 24 18"><rect width="24" height="18" rx="2" fill="#e4591f"/><path d="M2 3l10 7 10-7" fill="none" stroke="#fff" stroke-width="2"/></svg>info@mesaridge-roofing.com</div>
      <div class="contact"><svg width="7" height="7" viewBox="0 0 24 24"><circle cx="12" cy="12" r="11" fill="#e4591f"/><path d="M1 12h22M12 1c4 4 4 18 0 22M12 1c-4 4-4 18 0 22" fill="none" stroke="#fff" stroke-width="1.6"/></svg>www.mesaridge-roofing.com</div>
    </div>
  </div>
</section>

<!-- Back side -->
<section class="hanger hanger--back">
  <div class="photo back-photo" role="img" aria-label="Photo of a large stone and timber ranch home with a dark tile roof under a blue sky"></div>
  <div class="hole"></div>
  <div class="abs center brand-name" style="top:273px;font-size:27px;color:var(--ink)">Mesa Ridge Roofing</div>

  <svg class="chevrons" width="334" height="1000" viewBox="0 0 334 1000">
    <polygon points="0,543 256,424 334,463 334,1000 0,1000" fill="#1c1b1b"/>
    <polyline points="0,538 256,419 334,458" fill="none" stroke="#e4591f" stroke-width="8"/>
    <polyline points="0,480 82,444 140,470" fill="none" stroke="#e4591f" stroke-width="7"/>
  </svg>

  <div class="abs quality slab" style="top:476px">QUALITY<br>ROOFING</div>
  <div class="abs trust">YOU CAN TRUST</div>

  <svg class="types" width="334" height="125" viewBox="0 585 334 125">
    <defs>
      <linearGradient id="tileGrad" x1="0" y1="0" x2="0" y2="1"><stop offset="0" stop-color="#f08a4a"/><stop offset="1" stop-color="#d9541c"/></linearGradient>
      <linearGradient id="lowGrad" x1="0" y1="0" x2="0" y2="1"><stop offset="0" stop-color="#8aa6c6"/><stop offset=".45" stop-color="#3a3a36"/><stop offset=".55" stop-color="#a9b4c0"/><stop offset="1" stop-color="#6f7c8a"/></linearGradient>
      <linearGradient id="metalGrad" x1="0" y1="0" x2="0" y2="1"><stop offset="0" stop-color="#5d8fcf"/><stop offset=".35" stop-color="#4b5561"/><stop offset="1" stop-color="#2f3a44"/></linearGradient>
      <linearGradient id="shingleGrad" x1="0" y1="0" x2="0" y2="1"><stop offset="0" stop-color="#6f7380"/><stop offset="1" stop-color="#3f424c"/></linearGradient>
    </defs>
    <g stroke="#ffffff" stroke-width="2" stroke-linejoin="round">
      <polygon points="8,654 90,622 90,706 8,706" fill="url(#tileGrad)" role="img" aria-label="Photo of orange clay tile roofing"/>
      <polygon points="94,621 164,593 164,706 94,706" fill="url(#lowGrad)" role="img" aria-label="Photo of a low slope membrane roof"/>
      <polygon points="168,593 236,620 236,706 168,706" fill="url(#metalGrad)" role="img" aria-label="Photo of standing seam metal roofing"/>
      <polygon points="240,621 324,654 324,706 240,706" fill="url(#shingleGrad)" role="img" aria-label="Photo of grey asphalt shingle roofing"/>
    </g>
  </svg>
  <div class="type-label slab" style="left:48px">TILE</div>
  <div class="type-label slab" style="left:135px">LOW SLOPE</div>
  <div class="type-label slab" style="left:207px">METAL</div>
  <div class="type-label slab" style="left:289px">SHINGLE</div>

  <div class="phone-strip">
    <svg width="18" height="18" viewBox="0 0 24 24"><path fill="#e4591f" d="M6.6 10.8a15 15 0 0 0 6.6 6.6l2.2-2.2a1 1 0 0 1 1-.25 11.4 11.4 0 0 0 3.6.57 1 1 0 0 1 1 1V20a1 1 0 0 1-1 1A17 17 0 0 1 3 4a1 1 0 0 1 1-1h3.5a1 1 0 0 1 1 1c0 1.25.2 2.45.57 3.57a1 1 0 0 1-.25 1z"/></svg>
    <span>(555) 214-7730</span>
  </div>
  <div class="abs center back-address">1420 Pinecrest Ave, Alder AZ 86999</div>

  <div class="abs center brand-name back-brand">Mesa Ridge Roofing</div>
  <div class="abs center tagline">Residential Roofing Services</div>
</section>

</body>
</html>
```